San Francisco Pet Care Non Profit

Business Card Design for non profit organization.
We are a mobile pet care team who supports and attends to pets whose owners are homeless. Thanks for your help and creativity.

Industry/Entity Type

Non Profit

Contact Information for Business Card

Miriam Loxley
President
2817 Harrow Street, #516
San Francisco, CA 94187
phone: 415-782-3946
fax: 415-718-4053
miriam@warmpawvan.org
website: warmpawvan.org
facebook: facebook.com/WarmPawVan

Font styles to use
Serif
Sans Serif

Colors

Designer to choose colors to be used in the design.

Requirements
Must have
• above details and attached logo

```html
<!DOCTYPE html>
<html lang="en">
<head>
<meta charset="utf-8">
<title>WarmPawVan Business Card</title>
<link rel="stylesheet" href="https://fonts.googleapis.com/css2?family=Poppins:wght@500;600;700&family=Open+Sans:wght@400;600&display=swap">
<style>
  :root {
    --backdrop: #2b2e33;
    --card-white: #ffffff;
    --brand-blue: #1fa9e1;
    --ink-black: #1c1a1b;
    --text-dark: #2a2a2a;
    --address-blue: #34b8ea;
  }
  * { box-sizing: border-box; margin: 0; padding: 0; }
  html, body { width: 1200px; height: 900px; overflow: hidden; }
  body {
    background: var(--backdrop);
    position: relative;
    font-family: "Open Sans", sans-serif;
  }
  .card {
    position: absolute;
    top: 290px;
    width: 560px;
    height: 320px;
    border-radius: 18px;
    background: var(--card-white);
    overflow: hidden;
  }
  .card-front { left: 30px; }
  .card-back { left: 610px; }

  /* Front */
  .front-band-top {
    position: absolute; left: 0; top: 0; width: 100%; height: 42px;
    background: var(--brand-blue);
  }
  .front-band-bottom {
    position: absolute; left: 0; bottom: 0; width: 100%; height: 72px;
    background: var(--ink-black);
  }
  .front-brand {
    position: absolute; left: 56px; top: 92px;
    display: flex; align-items: center; gap: 18px;
  }
  .brand-dot {
    width: 62px; height: 62px; border-radius: 50%;
    border: 4px solid var(--brand-blue);
  }
  .brand-name {
    font-family: "Poppins", sans-serif;
    font-weight: 700;
    font-size: 50px;
    line-height: 1;
    color: var(--brand-blue);
    letter-spacing: -0.5px;
  }
  .front-tagline {
    position: absolute; left: 136px; top: 156px;
    font-family: "Poppins", sans-serif;
    font-weight: 600;
    font-size: 20px;
    color: var(--ink-black);
  }

  /* Back */
  .name-tab {
    position: absolute; left: 0; top: 22px;
    width: 330px; height: 58px;
    background: var(--ink-black);
    border-radius: 0 29px 29px 0;
    box-shadow: -20px 6px 0 var(--brand-blue);
    padding: 8px 0 0 40px;
  }
  .person-name {
    font-family: "Open Sans", sans-serif;
    font-weight: 600;
    font-size: 20px;
    line-height: 1.05;
    color: var(--brand-blue);
  }
  .person-title {
    font-size: 13px;
    color: var(--card-white);
  }
  .contact-list {
    position: absolute; left: 40px; top: 104px;
    list-style: none;
  }
  .contact-list li {
    display: flex; align-items: center; gap: 12px;
    font-size: 13.5px; color: var(--text-dark);
    height: 21px;
  }
  .contact-list svg { width: 14px; height: 14px; flex: none; }
  .social {
    position: absolute; left: 40px; top: 204px;
    display: flex; align-items: center; gap: 12px;
  }
  .social-dot {
    width: 18px; height: 18px; border-radius: 50%;
    background: var(--brand-blue);
  }
  .social-handle {
    font-weight: 600; font-size: 18px; color: var(--brand-blue);
  }
  .back-brand {
    position: absolute; left: 355px; top: 78px; width: 185px;
    display: flex; flex-direction: column; align-items: center; gap: 10px;
  }
  .back-brand .brand-dot { width: 96px; height: 96px; }
  .back-brand .brand-name { font-size: 26px; }
  .address-pill {
    position: absolute; right: 0; top: 244px;
    width: 290px; height: 58px;
    background: var(--address-blue);
    border-radius: 29px 0 0 29px;
    box-shadow: 20px -6px 0 var(--ink-black);
    padding: 9px 0 0 36px;
    font-size: 14px; line-height: 1.35; color: var(--text-dark);
  }
</style>
</head>
<body>

<section class="card card-front" aria-label="Business card front">
  <div class="front-band-top"></div>
  <div class="front-brand">
    <span class="brand-dot"></span>
    <span class="brand-name">WarmPawVan</span>
  </div>
  <p class="front-tagline">Mobile Pet Care Team</p>
  <div class="front-band-bottom"></div>
</section>

<section class="card card-back" aria-label="Business card back">
  <div class="name-tab">
    <p class="person-name">Miriam Loxley</p>
    <p class="person-title">President</p>
  </div>

  <ul class="contact-list">
    <li>
      <svg viewBox="0 0 16 16" aria-hidden="true"><path d="M3 1.5h3l1.2 3.3-1.8 1.2a9 9 0 0 0 4.6 4.6l1.2-1.8 3.3 1.2v3a1.5 1.5 0 0 1-1.6 1.5A13 13 0 0 1 1.5 3.1 1.5 1.5 0 0 1 3 1.5z" fill="#1fa9e1"/></svg>
      <span>415-782-3946</span>
    </li>
    <li>
      <svg viewBox="0 0 16 16" aria-hidden="true"><rect x="4" y="1.5" width="8" height="4" fill="none" stroke="#1fa9e1" stroke-width="1.5"/><rect x="1.5" y="5.5" width="13" height="6" rx="1" fill="#1fa9e1"/><rect x="4" y="10" width="8" height="4.5" fill="#fff" stroke="#1fa9e1" stroke-width="1.5"/></svg>
      <span>415-718-4053</span>
    </li>
    <li>
      <svg viewBox="0 0 16 16" aria-hidden="true"><rect x="1" y="3" width="14" height="10" rx="1" fill="#1fa9e1"/><path d="M1.5 3.8 8 8.8l6.5-5" fill="none" stroke="#fff" stroke-width="1.3"/></svg>
      <span>miriam@warmpawvan.org</span>
    </li>
    <li>
      <svg viewBox="0 0 16 16" aria-hidden="true"><g fill="none" stroke="#1fa9e1" stroke-width="1.4"><circle cx="8" cy="8" r="6.5"/><ellipse cx="8" cy="8" rx="3" ry="6.5"/><path d="M1.5 8h13"/></g></svg>
      <span>www.warmpawvan.org</span>
    </li>
  </ul>

  <div class="social">
    <span class="social-dot"></span>
    <span class="social-handle">WarmPawVan</span>
  </div>

  <div class="back-brand">
    <span class="brand-dot"></span>
    <span class="brand-name">WarmPawVan</span>
  </div>

  <address class="address-pill" style="font-style: normal;">
    2817 Harrow Street, #516<br>
    San Francisco, CA 94187
  </address>
</section>

</body>
</html>
```